Wine Label design for a Grapefruit flavored wine

We need a wine label for a wine that is flavored with grapefruit flavors and slightly sparkling.It should be eye catching and fun. It will be sold in the United States market. We like the idea of using a pink flamingo and/or grapefruits. Just one flamingo please if you use a flamingo. There is no size restriction on the label size. Something super eye catching and super fun.

Attached are some images we like, these are for your reference only, they are not good quality for print. You can choose to do something with a flamingo or with grapefruits or both together. Something bold is what we are looking for too. You can even use a clear label. We really don't mind seeing some fun and bold colors.

The name of the wine is: Vento di Calbrina
In small letters please put this sentence:

Grape wine with natural grapefruit, peach flavor, carbonation added
It is a white wine in a clear Bordeaux style bottle with a screw cap.

```html
<!DOCTYPE html>
<html lang="en">
<head>
<meta charset="utf-8">
<title>Vento di Calbrina – Wine Label</title>
<link rel="stylesheet" href="https://fonts.googleapis.com/css2?family=Poiret+One&family=Oswald:wght@400&display=swap">
<style>
  :root {
    --page-bg: #e4e3d9;
    --label-teal: #82cfd0;
    --label-teal-deep: #76c6c7;
    --title-yellow: #f3ec6c;
    --small-white: #f4f6f1;
    --flamingo-pink: #ec6a9b;
    --flamingo-light: #f4b2c9;
  }
  * { margin: 0; padding: 0; box-sizing: border-box; }
  html, body {
    width: 1200px;
    height: 1000px;
    overflow: hidden;
    background: var(--page-bg);
  }
  .canvas {
    position: relative;
    width: 1200px;
    height: 1000px;
  }
  .label {
    position: absolute;
    left: 341px;
    top: 60px;
    width: 518px;
    height: 880px;
    background: linear-gradient(180deg, var(--label-teal) 0%, var(--label-teal-deep) 100%);
    overflow: hidden;
  }
  .carbonation-note {
    position: absolute;
    left: 16px;
    top: 240px;
    transform: rotate(-90deg);
    transform-origin: left top;
    font-family: "Oswald", sans-serif;
    font-weight: 400;
    font-size: 12px;
    letter-spacing: 2.4px;
    color: var(--small-white);
    white-space: nowrap;
  }
  .flamingo-area {
    position: absolute;
    left: 54px;
    top: 67px;
    width: 408px;
    height: 755px;
    border-radius: 40%;
    background: radial-gradient(ellipse at 58% 42%,
      var(--flamingo-pink) 0%,
      var(--flamingo-light) 38%,
      rgba(130, 207, 208, 0) 72%);
  }
  .wine-name {
    position: absolute;
    left: 8px;
    top: 470px;
    width: 500px;
    height: 260px;
    overflow: visible;
  }
  .wine-name text {
    font-family: "Poiret One", sans-serif;
    fill: var(--title-yellow);
    font-size: 104px;
  }
  .wine-description {
    position: absolute;
    left: 17px;
    top: 766px;
    font-family: "Oswald", sans-serif;
    font-weight: 400;
    font-size: 17px;
    line-height: 27px;
    letter-spacing: 1.6px;
    color: var(--small-white);
    text-transform: uppercase;
  }
</style>
</head>
<body>
<main class="canvas">
  <section class="label">
    <p class="carbonation-note">CARBONATION ADDED</p>

    <div class="flamingo-area" role="img" aria-label="Watercolour illustration of a single pink flamingo standing on one leg"></div>

    <svg class="wine-name" viewBox="0 0 500 260" aria-label="Vento di Calbrina">
      <text x="0" y="112" textLength="312" lengthAdjust="spacingAndGlyphs">VENTO DI</text>
      <text x="0" y="244" textLength="491" lengthAdjust="spacingAndGlyphs">CALBRINA</text>
    </svg>

    <p class="wine-description">Grape wine with natural<br>grapefruit, peach flavor</p>
  </section>
</main>
</body>
</html>
```